Professional Home Buyer business card needed

I need a pretty straight forward business card designed. We help people that NEED to sell their homes solve problems. We perform all types of Real Estate transactions including flip, wholesale, investment, rental property and multi family. The card will mainly be used to give to prospective Sellers but will also be given to Real Estate Investors as well. It should professional and very easy to read, most clients are older people.

Target Market(s)

Distressed home sellers as well as Real Estate investors

Industry/Entity Type

Real Estate

Contact Information for Business Card

should be a professional layout

Colors
ec1f27
ffffff
000000

Requirements
Must have
• Large logo on back and smaller one on front. should utilize Red, white, and black.
• I am thinking of using a soft touch coating on the card so keep that in mind.
• Contact info should be very easy to read, think older clients.
Nice to have
• I would like to see a design with rounded corners on the card
Should not have
• pictures of homes or other home graphics.

```html
<!DOCTYPE html>
<html lang="en">
<head>
<meta charset="utf-8">
<title>Beacon Home Buyers – Business Card</title>
<link href="https://fonts.googleapis.com/css2?family=Arimo:wght@400;700&display=swap" rel="stylesheet">
<style>
  :root {
    --brand-red: #ec1f27;
    --ink: #000000;
    --paper: #ffffff;
    --stage: #d9d8da;
    --card-radius: 18px;
  }
  html, body {
    margin: 0;
    padding: 0;
    width: 1200px;
    height: 990px;
    overflow: hidden;
    background: var(--stage);
    font-family: "Arimo", Arial, sans-serif;
    color: var(--ink);
  }
  .sheet {
    width: 1200px;
    height: 990px;
    display: flex;
    align-items: center;
    justify-content: center;
    gap: 50px;
  }
  .card {
    position: relative;
    width: 540px;
    height: 300px;
    background: var(--paper);
    border-radius: var(--card-radius);
    box-sizing: border-box;
  }

  /* Front */
  .card--front { padding: 44px 32px 32px; }
  .holder__name {
    font-weight: 700;
    font-size: 21px;
    letter-spacing: -0.2px;
    margin: 0;
  }
  .holder__title {
    color: var(--brand-red);
    font-size: 14px;
    margin: 2px 0 0;
  }
  .brand-small {
    position: absolute;
    top: 44px;
    right: 32px;
    display: flex;
    flex-direction: column;
    align-items: center;
  }
  .brand-small__row {
    display: flex;
    align-items: center;
    gap: 10px;
  }
  .brand-small__mark {
    width: 16px;
    height: 16px;
    background: var(--brand-red);
  }
  .brand-small__name {
    font-weight: 700;
    font-size: 32px;
    letter-spacing: 1px;
    line-height: 1;
  }
  .brand-small__sub {
    font-weight: 700;
    font-size: 13px;
    letter-spacing: 3px;
    margin: 10px 0 0;
  }
  .contact {
    position: absolute;
    left: 32px;
    bottom: 34px;
    margin: 0;
    padding: 0;
    list-style: none;
    font-size: 15px;
    line-height: 21px;
  }
  .contact__label {
    color: var(--brand-red);
    display: inline-block;
    width: 26px;
  }
  .address {
    position: absolute;
    right: 32px;
    bottom: 34px;
    margin: 0;
    text-align: right;
    font-size: 15px;
    line-height: 21px;
    font-style: normal;
  }

  /* Back */
  .card--back {
    display: flex;
    flex-direction: column;
    align-items: center;
    justify-content: center;
  }
  .tagline {
    font-weight: 700;
    font-size: 15px;
    letter-spacing: 6px;
    margin: 0 0 26px;
  }
  .brand-large {
    display: flex;
    align-items: center;
    gap: 16px;
  }
  .brand-large__mark {
    width: 26px;
    height: 26px;
    background: var(--brand-red);
  }
  .brand-large__name {
    font-weight: 700;
    font-size: 58px;
    letter-spacing: 2px;
    line-height: 1;
  }
  .brand-large__sub {
    font-weight: 700;
    font-size: 26px;
    letter-spacing: 7px;
    margin: 22px 0 0;
  }
</style>
</head>
<body>
  <main class="sheet">
    <section class="card card--front" aria-label="Business card front">
      <h1 class="holder__name">DANIEL HARLOW</h1>
      <p class="holder__title">PRESIDENT</p>

      <div class="brand-small">
        <div class="brand-small__row">
          <span class="brand-small__mark"></span>
          <span class="brand-small__name">BEACON</span>
        </div>
        <p class="brand-small__sub">HOME BUYERS</p>
      </div>

      <ul class="contact">
        <li><span class="contact__label">t -</span>316-555-0148</li>
        <li><span class="contact__label">e -</span>daniel@beaconoffers.net</li>
        <li><span class="contact__label">w -</span>www.beaconoffers.net</li>
      </ul>

      <address class="address">P.O. Box 112<br>Maple Ridge, KS 67000</address>
    </section>

    <section class="card card--back" aria-label="Business card back">
      <p class="tagline">SELLING MADE SIMPLE!</p>
      <div class="brand-large">
        <span class="brand-large__mark"></span>
        <span class="brand-large__name">BEACON</span>
      </div>
      <p class="brand-large__sub">HOME BUYERS</p>
    </section>
  </main>
</body>
</html>
```